Roll Up Banner for Lifestyle / medical company

I need a roll-up banner for a congress highlighting our lifestyle company that aids people with diabetes type 2 through diet and exercise. The banner should capture our unique approach and appeal to medical professionals.

120x200 cm

Scope of work
- Design a roll-up banner for a congress.
- Include the programme name: Ons Suikerpad Route Schema.
- Add the catchphrase: Het individuele leefstijlprogramma voor 50-plussers met diabetes type 2.
- Feature the 4 pillars: Digitaal en persoonlijk, Duurzame begeleiding, Bewezen resultaten, Aanvulling ketenzorg.

References
- See our style at voedwijzerkracht.nl and in the files attached

Additional information
The banner should appeal to medical professionals attending the congress.

Company details
- Company website: voedwijzerkracht.nl
- We are a lifestyle company dedicated to helping people manage diabetes type 2 through tailored diet and exercise programs. Our target audience for this banner is medical professionals.

We can provide photo's of older individuals in our style. Contact us at info@voedwijzerkracht.nl for these pictures.

```html
<!DOCTYPE html>
<html lang="nl">
<head>
<meta charset="utf-8">
<title>Ons Suikerpad Route Schema – Roll-up banner</title>
<link rel="stylesheet" href="https://fonts.googleapis.com/css2?family=League+Gothic&family=Montserrat:wght@600;700;800&display=swap">
<style>
  :root {
    --teal: #069e98;
    --teal-light: #19c2b7;
    --green-dark: #0d4a3e;
    --paper: #e8e8e8;
    --backdrop: #4d4d4d;
    --white: #ffffff;
  }
  * { box-sizing: border-box; margin: 0; padding: 0; }
  html, body { width: 966px; height: 1200px; overflow: hidden; background: var(--backdrop); }
  .canvas { position: relative; width: 966px; height: 1200px; }
  .banner {
    position: absolute; left: 247px; top: 30px;
    width: 471px; height: 1140px;
    background: var(--paper); overflow: hidden;
    font-family: "Montserrat", sans-serif; color: var(--green-dark);
  }
  .banner-shapes { position: absolute; inset: 0; }
  .brand {
    position: absolute; left: 0; right: 0; top: 76px;
    display: flex; align-items: center; justify-content: center; gap: 8px;
  }
  .brand-square { width: 16px; height: 16px; background: var(--green-dark); border-radius: 3px; }
  .brand-name { font-weight: 800; font-size: 23px; letter-spacing: -0.3px; color: var(--green-dark); }
  .programme-title {
    position: absolute; left: 14px; top: 314px;
    font-family: "League Gothic", sans-serif; font-weight: 400;
    color: var(--white); font-size: 58px; line-height: 58px; text-transform: uppercase;
  }
  .programme-title span { display: block; }
  .programme-title span + span { margin-top: 2px; font-size: 62px; }
  .tagline {
    position: absolute; left: 0; right: 0; top: 552px;
    text-align: center; font-weight: 700; line-height: 1.08;
  }
  .tagline .l1 { display: block; font-size: 35px; }
  .tagline .l2 { display: block; font-size: 28px; }
  .tagline .l3 { display: block; font-size: 32px; }
  .tagline .l4 { display: block; font-size: 26px; }
  .pillar {
    position: absolute; width: 195px; height: 140px;
    border: 6px solid var(--teal); border-radius: 18px; background: var(--paper);
    text-align: center;
  }
  .pillar svg { display: block; margin: 8px auto 0; width: 54px; height: 54px; }
  .pillar-label { margin-top: 6px; font-weight: 700; font-size: 18.5px; line-height: 1.1; }
  .pillar--digital { left: 27px; top: 738px; }
  .pillar--guidance { left: 247px; top: 738px; }
  .pillar--results { left: 27px; top: 908px; }
  .pillar--chain { left: 247px; top: 908px; }
  .contact {
    position: absolute; left: 0; right: 0; top: 1106px;
    text-align: center; color: var(--white);
    font-weight: 600; font-size: 16px; letter-spacing: 2.2px;
  }
</style>
</head>
<body>
<div class="canvas">
  <div class="banner">
    <svg class="banner-shapes" viewBox="0 0 471 1140" width="471" height="1140">
      <defs>
        <linearGradient id="portraitTone" x1="0" y1="0" x2="0" y2="1">
          <stop offset="0" stop-color="#d9d6d2"/>
          <stop offset="0.3" stop-color="#c99a7e"/>
          <stop offset="0.42" stop-color="#d78a34"/>
          <stop offset="0.55" stop-color="#1c4a42"/>
          <stop offset="1" stop-color="#15403a"/>
        </linearGradient>
      </defs>
      <path class="hero-band" d="M0 126 Q235 274 471 126 L471 588 Q235 412 0 588 Z" fill="var(--teal)"/>
      <g class="hero-lines" fill="none" stroke="var(--teal-light)" stroke-width="4" stroke-linecap="round">
        <path d="M22 373 H214 Q221 373 221 366 V222 Q221 214 228 214 Q235 214 235 222 V520"/>
        <path d="M272 300 V270 Q272 236 306 236 H330"/>
        <path d="M466 312 Q458 312 458 322 V420"/>
      </g>
      <circle cx="22" cy="373" r="5" fill="var(--teal-light)"/>
      <path class="portrait" role="img" aria-label="Portretfoto van een glimlachende vrouw van rond de zestig met kort grijs haar, donkergroen colbert en oranje sjaal, armen over elkaar"
            d="M300 148 Q340 142 370 150 L471 180 L471 600 L240 600 L240 230 Q250 170 300 148 Z" fill="url(#portraitTone)"/>
      <path class="content-panel" d="M0 588 Q235 412 471 588 L471 1140 L0 1140 Z" fill="var(--paper)"/>
      <path class="footer-band" d="M0 1092 Q235 1054 471 1092 L471 1140 L0 1140 Z" fill="var(--teal)"/>
    </svg>

    <div class="brand">
      <span class="brand-square"></span>
      <span class="brand-name">voedwijzerkracht</span>
    </div>

    <h1 class="programme-title"><span>Ons Suikerpad</span><span>Route Schema</span></h1>

    <p class="tagline">
      <span class="l1">Het individuele</span>
      <span class="l2">leefstijlprogramma</span>
      <span class="l3">voor 50-plussers</span>
      <span class="l4">met diabetes type 2</span>
    </p>

    <div class="pillar pillar--digital">
      <svg viewBox="0 0 54 54" fill="none" stroke="var(--green-dark)" stroke-width="3.4" stroke-linecap="round" stroke-linejoin="round">
        <circle cx="22" cy="10" r="7"/>
        <path d="M8 40 V34 Q8 22 22 22 Q30 22 34 27"/>
        <path d="M8 40 H28"/>
        <rect x="32" y="30" width="14" height="22" rx="2"/>
        <circle cx="39" cy="46" r="0.8" fill="var(--green-dark)"/>
      </svg>
      <p class="pillar-label">Digitaal en<br>persoonlijk</p>
    </div>

    <div class="pillar pillar--guidance">
      <svg viewBox="0 0 54 54" fill="var(--green-dark)">
        <rect x="24" y="12" width="6" height="40"/>
        <path d="M27 2 L36 12 H18 Z"/>
        <path d="M27 34 Q27 24 14 20 L16 16 Q31 20 31 34 Z"/>
        <path d="M4 18 L16 10 L16 26 Z"/>
        <path d="M27 34 Q27 24 40 20 L38 16 Q23 20 23 34 Z"/>
        <path d="M50 18 L38 10 L38 26 Z"/>
      </svg>
      <p class="pillar-label">Duurzame<br>begeleiding</p>
    </div>

    <div class="pillar pillar--results">
      <svg viewBox="0 0 54 54" fill="none" stroke="var(--green-dark)" stroke-width="3.2" stroke-linecap="round" stroke-linejoin="round">
        <path d="M30 46 H10 Q6 46 6 42 V6 Q6 2 10 2 H30 Q36 2 36 8 V26"/>
        <path d="M13 12 H29 M13 19 H29 M13 26 H25 M13 33 H22"/>
        <circle cx="40" cy="40" r="11"/>
        <path d="M35 40 L39 44 L46 36"/>
      </svg>
      <p class="pillar-label">Bewezen<br>resultaten</p>
    </div>

    <div class="pillar pillar--chain">
      <svg viewBox="0 0 54 54" fill="none" stroke="var(--green-dark)" stroke-width="3.4" stroke-linecap="round" stroke-linejoin="round">
        <path d="M27 48 L8 30 Q1 22 5 13 Q10 4 20 6 Q24 7 27 11 Q30 7 34 6 Q44 4 49 13 Q53 22 46 30 Z"/>
        <rect x="10" y="19" width="20" height="11" rx="5.5"/>
        <rect x="24" y="19" width="20" height="11" rx="5.5"/>
      </svg>
      <p class="pillar-label">Aanvulling<br>ketenzorg.</p>
    </div>

    <p class="contact">info@voedwijzerkracht.nl</p>
  </div>
</div>
</body>
</html>
```